Quarvelon stickers design for our main topics (for example: agile and Kanban)

We are looking for sticker design, that will reflect our cooperate identity and can be used for the different topics in our company. We would like to start with our Agile Coaching Offers with a Kanban Sticker saying "stop starting, start finishing", A bad example can be find in the file upload ;)
Check out our homepage to get a feeling for the cooperate identity (www.quarvelon-beispiel.ch)

Target Market(s)

Customers and trainees from our trainings

Industry/Entity Type

Consulting

Colors
0355a3
fbed22

Requirements
Must have
• a cool design thats fits to our customer design
the 2 lines can be changed for future stickers ... like in the example "stop starting, start finishing" and "we show you how"
Nice to have
• -
Should not have
• -

```html
<!DOCTYPE html>
<html lang="en">
<head>
<meta charset="utf-8">
<title>Quarvelon Sticker – Stop Starting, Start Finishing</title>
<link rel="stylesheet" href="https://fonts.googleapis.com/css2?family=Russo+One&family=Michroma&family=Open+Sans:wght@300&display=swap">
<style>
  :root {
    --backdrop: #92bde6;
    --sticker: #ffffff;
    --brand-blue: #3a56a6;
    --brand-yellow: #f7f59e;
    --ink: #111111;
  }
  html, body {
    margin: 0;
    padding: 0;
    width: 1200px;
    height: 1084px;
    overflow: hidden;
    background: var(--backdrop);
  }
  .canvas {
    position: relative;
    width: 1200px;
    height: 1084px;
  }
  .sticker {
    position: absolute;
    left: 0;
    top: 0;
  }
  .headline-heavy {
    font-family: "Russo One", "Arial Black", sans-serif;
  }
  .headline-light {
    font-family: "Michroma", "Arial", sans-serif;
  }
  .company-name {
    font-family: "Open Sans", "Helvetica", sans-serif;
    font-weight: 300;
  }
</style>
</head>
<body>
<main class="canvas">
  <svg class="sticker" width="1200" height="1084" viewBox="0 0 1200 1084" role="img" aria-label="Sticker: Stop starting, start finishing – Quarvelon ag">
    <rect class="sticker-card" x="296" y="212" width="581" height="638" rx="44" fill="var(--sticker)"/>

    <!-- STOP line -->
    <text class="headline-heavy stop-word" x="340" y="358" font-size="137" fill="var(--brand-blue)" textLength="206" lengthAdjust="spacingAndGlyphs">ST</text>
    <g class="power-icon">
      <circle cx="643" cy="310" r="55" fill="var(--brand-blue)"/>
      <path d="M622 286 A30 30 0 1 0 664 286" fill="none" stroke="var(--brand-yellow)" stroke-width="11" stroke-linecap="round"/>
      <line x1="643" y1="270" x2="643" y2="306" stroke="var(--brand-yellow)" stroke-width="11" stroke-linecap="round"/>
    </g>
    <text class="headline-heavy stop-word" x="735" y="358" font-size="137" fill="var(--brand-blue)" textLength="97" lengthAdjust="spacingAndGlyphs">P</text>

    <!-- STARTING -->
    <text class="headline-light" x="340" y="441" font-size="70" fill="var(--ink)" textLength="488" lengthAdjust="spacingAndGlyphs">STARTING</text>

    <!-- START band -->
    <rect class="start-band" x="338" y="477" width="497" height="107" fill="var(--brand-blue)"/>
    <text class="headline-heavy" x="358" y="570" font-size="103" fill="var(--brand-yellow)" textLength="464" lengthAdjust="spacingAndGlyphs">START</text>

    <!-- FINISHING -->
    <text class="headline-light" x="340" y="660" font-size="76" fill="var(--ink)" textLength="495" lengthAdjust="spacingAndGlyphs">FINISHING</text>

    <!-- divider -->
    <line class="divider" x1="341" y1="684" x2="834" y2="684" stroke="var(--brand-blue)" stroke-width="3"/>

    <!-- company signature -->
    <rect class="company-square" x="440" y="712" width="54" height="54" fill="var(--brand-blue)"/>
    <text class="company-name" x="508" y="735" font-size="40" fill="var(--ink)">quarvelon ag</text>
  </svg>
</main>
</body>
</html>
```